Broschüre für Anbieter von Hundespielzeug und -snacks
Zielgruppe
wir werden einen Onlineshop eröffnen für enrichment Hundespielzeug und gesunde snacks. Das ganze ist seine based und in unserer dog daycare täglich getestet von echten Hunden.
Aufgabenstellung
es sollte alles in einem seine based lab design mit den Farben Blau, weiss, hellgrau gehalten werden. eventuell noch gelb und rot. ich liefere alle Texte.

```html
<!DOCTYPE html>
<html lang="en">
<head>
<meta charset="utf-8">
<title>Paws & Pantry – Lab Cookbook Spread</title>
<link href="https://fonts.googleapis.com/css2?family=Montserrat:wght@500;600&family=Open+Sans:ital,wght@0,400;0,600;0,700;1,400&display=swap" rel="stylesheet">
<style>
  :root {
    --backdrop: #e4e5e7;
    --paper: #f6f6f7;
    --paper-shade: #ebecee;
    --teal: #168a9e;
    --teal-light: #3fa9b8;
    --navy: #134a70;
    --navy-deep: #0e3a5c;
    --heading: #1c4f7d;
    --ink: #2a2e33;
    --body: #6a6e74;
  }
  * { box-sizing: border-box; margin: 0; padding: 0; }
  html, body { width: 1200px; height: 818px; overflow: hidden; }
  body {
    background: var(--backdrop);
    font-family: "Open Sans", Arial, sans-serif;
    color: var(--body);
    position: relative;
  }
  .spread {
    position: absolute;
    left: 40px; top: 24px;
    width: 1120px; height: 770px;
    display: flex;
    box-shadow: 0 8px 24px rgba(0,0,0,.12);
  }
  .page {
    position: relative;
    width: 560px; height: 770px;
    background: var(--paper);
    overflow: hidden;
  }
  .page--left { background: linear-gradient(90deg, var(--paper) 85%, var(--paper-shade)); }
  .page--right { background: linear-gradient(90deg, var(--paper-shade), var(--paper) 14%); }
  .page svg.art { position: absolute; left: 0; top: 0; }

  .heading {
    font-family: "Montserrat", Arial, sans-serif;
    font-weight: 500;
    color: var(--heading);
    text-transform: uppercase;
    letter-spacing: .04em;
  }
  .intro { position: absolute; left: 34px; top: 368px; width: 500px; }
  .intro .heading { font-size: 20px; margin-bottom: 8px; }
  .copy { font-size: 10.5px; line-height: 1.5; }
  .protocols { position: absolute; left: 34px; top: 496px; width: 500px; }
  .protocols .heading { font-size: 20px; margin-bottom: 4px; }
  .protocols .lead {
    font-family: "Montserrat", Arial, sans-serif;
    font-weight: 500; color: var(--ink); font-size: 14px; margin-bottom: 9px;
  }
  .protocols .copy { margin-bottom: 7px; }
  .protocols strong { color: var(--heading); font-weight: 700; font-style: italic; }

  .formula { position: absolute; left: 30px; top: 36px; width: 500px; }
  .formula .title {
    font-family: "Montserrat", Arial, sans-serif;
    font-weight: 500; color: var(--heading); font-size: 17px; margin-bottom: 4px;
  }
  .formula .title span { text-transform: uppercase; letter-spacing: .04em; }
  .formula .copy { font-size: 9.5px; }

  .recipe { position: absolute; left: 36px; width: 500px; height: 112px; }
  .recipe .photo {
    position: absolute; left: 0; top: 0;
    width: 104px; height: 104px; border-radius: 50%;
  }
  .recipe .text { position: absolute; left: 136px; top: 6px; width: 360px; }
  .recipe .name {
    font-family: "Montserrat", Arial, sans-serif;
    font-weight: 500; color: var(--heading); font-size: 15px; margin-bottom: 4px;
  }
  .recipe .label {
    font-family: "Montserrat", Arial, sans-serif;
    font-weight: 600; color: var(--heading); font-size: 11px;
  }
  .recipe .copy { font-size: 9.5px; line-height: 1.4; }

  .photo--fritters { background: radial-gradient(circle at 55% 55%, #d48a3a, #c46a2c 55%, #b8c4a0); }
  .photo--yogurt { background: radial-gradient(circle, #f4f2ee 45%, #7a4a34 60%, #5c3826); }
  .photo--kibble { background: radial-gradient(circle, #9a9a5a, #7b7744 60%, #8a8a70); }
  .photo--carrot { background: linear-gradient(160deg, #e06a3a, #d88a5a 50%, #6c7a3a); }
</style>
</head>
<body>
<main class="spread">

  <section class="page page--left">
    <svg class="art" width="560" height="770" viewBox="0 0 560 770">
      <defs>
        <linearGradient id="tealGrad" x1="0" y1="0" x2="1" y2="0">
          <stop offset="0" stop-color="#0f7f94"/>
          <stop offset="1" stop-color="#44abba"/>
        </linearGradient>
        <linearGradient id="footGrad" x1="0" y1="0" x2="1" y2="0">
          <stop offset="0" stop-color="#0e3a5c"/>
          <stop offset="1" stop-color="#5a86a3"/>
        </linearGradient>
        <clipPath id="heroClip">
          <path d="M0,0 H560 V250 C530,215 490,170 430,170 C350,172 300,300 190,330 C100,352 25,310 0,250 Z"/>
        </clipPath>
      </defs>
      <path class="hero-band" fill="url(#tealGrad)" d="M0,0 H560 V250 C530,215 490,170 430,170 C350,172 300,300 190,330 C100,352 25,310 0,250 Z"/>
      <g role="img" aria-label="Photo of the two daycare founders with three black dogs and a dog leaping for a flying disc" clip-path="url(#heroClip)">
        <rect x="0" y="40" width="440" height="310" fill="#1c7f90" opacity=".55"/>
      </g>
      <path class="foot-band" fill="url(#footGrad)" d="M0,754 C200,750 420,740 560,726 V770 H0 Z"/>
    </svg>

    <div class="intro">
      <h1 class="heading">Welcome to the Lab</h1>
      <p class="copy">Congratulations, you are now a certified Paws &amp; Pantry Lab Technician. You hold in your hands the official cookbook, the result of extensive research into canine enrichment and mental well-being. This is not just food; it's a tool for behavioral optimization.<br>Your mission: synthesis these potent formulas and deploy them via the specialized enrichment devices (toys) included in your box to unlock your dog's potential.</p>
    </div>

    <div class="protocols">
      <h2 class="heading">Important Laboratory Protocols</h2>
      <p class="lead">Before initiating synthesis, review these critical safety directives:</p>
      <p class="copy"><strong>Safety First:</strong> Ensure ALL ingredients are 100% dog-safe. NEVER use xylitol (a common sweetener in peanut butter), grapes, raisins, onions, garlic, chocolate, or macadamia nuts.</p>
      <p class="copy">Technician Discretion: Always consult your veterinarian before introducing new foods or supplements, especially for dogs with existing health conditions or known allergies.</p>
      <p class="copy">The "Work" Phase: The secret is in the temperature. Freezing a loaded enrichment device dramatically increases the "work" required, providing a superior cognitive challenge.</p>
      <p class="copy">Calorie Calibration: Adjust your dog's main meal portions to account for the calories synthesized in these enrichment formulas. Over-calibration is a lab violation.</p>
    </div>
  </section>

  <section class="page page--right">
    <svg class="art" width="560" height="770" viewBox="0 0 560 770">
      <path class="foot-band" fill="#134a70" d="M0,770 V730 C160,660 360,615 560,600 V770 Z"/>
      <g role="img" aria-label="Two large faint paw print decorations">
        <rect x="320" y="655" width="170" height="80" rx="36" fill="#2a6190" opacity=".35"/>
      </g>
    </svg>

    <div class="formula">
      <h2 class="title"><span>Formula P</span> | Development</h2>
      <p class="copy">Primary Objective: Accelerated Cognitive Growth &amp; Optimized Teething Relief The "Neuron-Nutrient-Booster" – engineered for growing brain matter and achy, developing jaws.</p>
    </div>

    <article class="recipe" style="top:108px">
      <div class="photo photo--fritters" role="img" aria-label="Photo of golden sweet potato bites with dipping sauce"></div>
      <div class="text">
        <h3 class="name">SYNT-1. "Puppy Brain Builder"</h3>
        <p class="label">Ingredients:</p>
        <p class="copy">100g Cooked Sweet Potato (mashed, no skins)<br>1 tbsp Salmon Oil (critical for Omega-3 fatty acid infusion)<br>5-6 Blueberries (antioxidant deployment)<br>A few soaked rolled oats (for texture variable)</p>
      </div>
    </article>

    <article class="recipe" style="top:224px">
      <div class="photo photo--yogurt" role="img" aria-label="Photo of a bowl of plain yogurt with a wooden spoon"></div>
      <div class="text">
        <h3 class="name">SYNT-2. "Teething Relief Puree"</h3>
        <p class="label">Ingredients:</p>
        <p class="copy">100g Plain Greek Yogurt (low-fat, unsweetened)<br>1 tbsp Pumpkin Puree (pure canned pumpkin, NOT pie filling)<br>1 tsp Coconut Oil (melted and cooled)</p>
      </div>
    </article>

    <article class="recipe" style="top:340px">
      <div class="photo photo--kibble" role="img" aria-label="Photo of a pile of green dried dog treats"></div>
      <div class="text">
        <h3 class="name">SYNT-3. "The Forager" Dry Mix</h3>
        <p class="label">Ingredients:</p>
        <p class="copy">Handful of freeze-dried beef or lamb liver (crumbled)<br>Handful of air-dried sweet potato chips (crumbled)<br>A few high-quality, small-breed puppy kibble pieces</p>
      </div>
    </article>

    <article class="recipe" style="top:456px">
      <div class="photo photo--carrot" role="img" aria-label="Photo of baked carrot treat sticks with fresh carrots"></div>
      <div class="text">
        <h3 class="name">SYNT-4. "Brainy Bites" Challenge</h3>
        <p class="label">Ingredients:</p>
        <p class="copy">Handful of small, grain-free puppy treats<br>A few raw baby carrot sticks (halved)</p>
      </div>
    </article>
  </section>

</main>
</body>
</html>
```